依頼詳細
表面には、東谷工務【ベルモーラ】のロゴを入れて頂きたいです。
老眼の人にも見えやすい文字の大きさと色で文字はお願いいたします。
電話をされる方が多いので電話の文字は大きめでお願いします。
裏面は不在の家の方へメッセージを書くので1/4ほど空欄が欲しいです。
裏面に、東谷工務(ベルモーラ)の想いと、規格住宅ハーモニーワンのロゴとコンセプトがあれば嬉しいです。
記載項目
表面:東谷工務株式会社。
住所:福山市松永町大字高見1438番地
電話番号:084-637-4190
http://www.higashitani-koumu.jp
E-mail:contact@higashitani-koumu.jp
〒720-0492
名前:代表取締役:東谷康弘(ひがしたにやすひろ)
名前:主任:小柳武志(こやなぎたけし)
名前:コーディネート:岡部理恵(おかべりえ)
名前:設計:古川ゆみ(ふるかわゆみ)
裏面:東谷康弘:1級建築士:宅地建物取引主任者:住宅ローンアドバイザー
小柳武志:2級建築士
ベルモーラのコンセプト:注文住宅とリフォームの【ベルモーラ】東谷工務と熟練したスキルをもつ専門家がチームを組みお客様をサポートします!
ハーモニーワン:ちょうどいい暮らしにプラスした規格住宅。中四国でトップクラスの住宅性能を20代の家族でも手の届く価格で提供しています。
希望イメージ
シンプル 複雑
単色 カラフル
暗い 明るい
日常 高級
遊び心 厳粛
未来的 伝統的
女性的 男性的
希望する色
緑系
納品ファイル
• 高解像度JPG (.jpg)
• イラストレーター形式 (.ai)
補足説明
歴史がありますが、若い世代を中心に活動を行っています。常に新しい事を取り入れて、熟練職人と試行錯誤をしながら家創りを行っています。
■ 選んだ理由

皆様にお詫びをしなければならない事があります。
インターネットの不具合があり、昨日やっと復旧することが出来ました。決定が遅くなり申し訳ありませんでした。今回の選定には、表面には『分かり易さ』を主にしていました。名刺を渡したときに、会社の名前と業種が分かり、名前と役職が一瞬で判断できるもので、優れているデザインを選びました。裏面においては、メッセージが書きやすく目立つようになっている事。ハーモニーワンとベルモーラの違いがさらっと分かり易いモノを選ばせていただきました。

■ 提案者全員のお礼・コメント

皆様ひとりひとりに特徴があり、取り入れたいモノが沢山あり学びとなりました。共栄会の会合に参加して、沢山の会社の方と名刺交換をし、どういう意図で名刺を作っているかを聞いてそれも参考にさせて頂きました。会社の中では色を決め切ることが出来なかった(みんなバラバラ)でしたので、6色バージョンを作成してもらい、それぞれに選んでもらう事としました。
とても満足しています。皆様本当にありがとうございました。
東谷工務 代表取締役 東谷康弘より

```html
<!DOCTYPE html>
<html lang="ja">
<head>
<meta charset="utf-8">
<title>東谷工務株式会社 名刺</title>
<link rel="stylesheet" href="https://fonts.googleapis.com/css2?family=Noto+Sans+JP:wght@400;500;700&family=M+PLUS+Rounded+1c:wght@400;500&display=swap">
<style>
  :root {
    --olive: #8d8b4e;
    --paper: #ffffff;
    --ink: #2b2b2b;
    --ink-soft: #4a4a4a;
  }
  * { margin: 0; padding: 0; box-sizing: border-box; }
  html, body { width: 729px; height: 1200px; overflow: hidden; background: var(--paper); }
  .card {
    position: relative;
    width: 729px;
    height: 1200px;
    background: var(--paper);
    font-family: "Noto Sans JP", sans-serif;
    color: var(--ink);
    overflow: hidden;
  }
  .card__band { position: absolute; left: 0; top: 0; width: 729px; height: 700px; }
  .brand {
    position: absolute;
    left: 0; top: 270px;
    width: 729px;
    display: flex;
    align-items: center;
    justify-content: center;
    gap: 34px;
    color: var(--paper);
  }
  .brand__mark {
    width: 40px; height: 40px;
    border: 5px solid var(--paper);
  }
  .brand__name {
    font-family: "Noto Sans JP", sans-serif;
    font-weight: 700;
    font-size: 72px;
    letter-spacing: 4px;
    line-height: 1;
  }
  .brand__kana {
    position: absolute;
    left: 0; top: 395px;
    width: 729px;
    text-align: center;
    color: var(--paper);
    font-weight: 700;
    font-size: 36px;
    letter-spacing: 6px;
  }
  .person {
    position: absolute;
    left: 218px; top: 735px;
    width: 400px;
    text-align: center;
  }
  .person__role { font-size: 29px; font-weight: 500; letter-spacing: 2px; }
  .person__name { margin-top: 8px; font-size: 50px; font-weight: 700; letter-spacing: 6px; line-height: 1.2; }
  .person__name span { margin-left: 48px; }
  .person__roman {
    margin-top: 2px;
    font-family: "M PLUS Rounded 1c", sans-serif;
    font-size: 27px;
    color: var(--ink-soft);
    letter-spacing: 1px;
  }
  .company {
    position: absolute;
    left: 42px; top: 968px;
    font-size: 30px;
    font-weight: 500;
    letter-spacing: 1px;
  }
  .contact {
    position: absolute;
    left: 312px; top: 960px;
    font-size: 23px;
    line-height: 43px;
  }
  .contact__tel { font-size: 37px; letter-spacing: 2px; line-height: 50px; margin-bottom: 4px; }
  .contact__line { font-weight: 500; }
</style>
</head>
<body>
  <div class="card">
    <svg class="card__band" viewBox="0 0 729 700" aria-hidden="true">
      <path d="M0 0 H729 V612 C650 590 560 600 470 632 C370 668 300 690 200 672 C120 658 60 640 0 652 Z" fill="var(--olive)"/>
    </svg>

    <div class="brand">
      <span class="brand__mark"></span>
      <span class="brand__name">BELMORA</span>
    </div>
    <div class="brand__kana">ベルモーラ</div>

    <div class="person">
      <p class="person__role">代表取締役</p>
      <p class="person__name">東谷<span>康弘</span></p>
      <p class="person__roman">-yasuhiro higashitani-</p>
    </div>

    <p class="company">東谷工務株式会社</p>

    <div class="contact">
      <p class="contact__tel">TEL：084-637-4190</p>
      <p class="contact__line">〒720-0492</p>
      <p class="contact__line">福山市松永町大字高見 1438 番地</p>
      <p class="contact__line">http://www.higashitani-koumu.jp</p>
      <p class="contact__line">contact@higashitani-koumu.jp</p>
    </div>
  </div>
</body>
</html>
```